Eye Catching Email Marketing design

Our health care consulting firm is based in New York City. We sell health care consulting Services to medical practices (doctors). We need a powerful email marketing design to use as one of our primary selling tools to attract new clients. The Design should convey health care knowledge, expertise professionalism, cutting edge technology and the services we offer. <br/>The design should incorporate our logo and its colors (blue and white) but we want it to be eye catching and vibrant, so other colors be included. We are open to the designer's creativity. Any pictures used should show diversity (races)and should include women. Designers can find our logo and other graphics on our website at www harbor crest advisory.com. Please feel free to ask questions.<br/><br/>

Target Market(s)

Health care professionals, executives and Doctors.

Colors

Designer to choose colors to be used in the design.

Requirements
Nice to have
• What ever the design feels will help make this design vibrant

```html
<!DOCTYPE html>
<html lang="en">
<head>
<meta charset="utf-8">
<title>Harbor Crest Advisory – Newsletter</title>
<link href="https://fonts.googleapis.com/css2?family=Titillium+Web:wght@400;600;700;900&display=swap" rel="stylesheet">
<style>
  :root{
    --page:#eef1f4;
    --blue:#0f84dc;
    --blue-deep:#1a6fd6;
    --blue-sea:#0a9ad6;
    --navy:#10407f;
    --footer:#0b74b8;
    --yellow:#ffe600;
    --yellow-pale:#fff3a6;
    --ink:#1e2a36;
    --grey:#5f6870;
    --link:#1c6fc4;
    --white:#ffffff;
  }
  *{box-sizing:border-box;margin:0;padding:0}
  html,body{width:1102px;height:1200px;overflow:hidden;background:var(--page)}
  body{font-family:"Titillium Web",sans-serif;position:relative}
  .newsletter{
    position:absolute;left:231px;top:0;width:692px;height:1295px;
    transform:scale(0.926);transform-origin:top left;
    background:var(--white);overflow:hidden;
  }
  .abs{position:absolute}
  .preheader{left:22px;top:14px;width:360px;font-size:12.5px;line-height:19px;color:var(--grey)}
  .preheader-right{left:460px;top:16px;font-size:12.5px;line-height:19px;color:var(--grey)}
  .preheader-right a{color:var(--link);text-decoration:none;font-size:14px}
  .hero-bg{left:0;top:72px;width:692px;height:900px;
    background:linear-gradient(160deg,#ffffff 0%,#f4f9fd 45%,#dcecf7 75%,#cfe4f3 100%)}
  .shapes{left:0;top:0}
  .brand{left:16px;top:150px;width:270px;display:flex;align-items:center;gap:10px;
    font-size:19px;font-weight:700;color:var(--navy);letter-spacing:.3px;text-transform:uppercase}
  .brand-dot{width:16px;height:16px;border-radius:50%;background:var(--navy);flex:none}
  .photo{left:0;top:225px;width:345px;height:500px;border-radius:0 0 40px 0;
    background:radial-gradient(ellipse at 45% 35%,#f2ede8 0%,#e9e4e0 40%,#d9dde2 70%,rgba(220,232,242,0) 100%)}
  .headline{left:344px;top:86px;color:var(--white);font-weight:700;text-transform:uppercase;line-height:1}
  .headline span{display:block}
  .hl-welcome{font-size:66px;letter-spacing:1px}
  .hl-name{font-size:55px;margin-top:4px}
  .hl-accent{font-size:88px;color:var(--yellow);font-weight:900;margin-top:0}
  .hl-tail{font-size:58px;color:var(--yellow-pale);margin-top:2px}
  .help-title{left:363px;top:512px;font-size:31px;font-weight:700;line-height:43px;color:var(--ink)}
  .service{position:absolute;width:150px;font-size:17px;line-height:23px;color:var(--ink)}
  .service-icon{width:52px;height:52px;border-radius:10px;margin-bottom:12px}
  .call{left:27px;top:695px;width:250px;height:250px;border-radius:50%;
    background:var(--blue);border:5px solid var(--white);
    display:flex;flex-direction:column;align-items:center;justify-content:center;color:var(--white);
    box-shadow:0 4px 14px rgba(10,60,120,.25)}
  .call-label{font-size:31px;font-weight:700;line-height:32px;margin-top:8px}
  .call-number{font-size:26px;font-weight:700;line-height:32px}
  .lower{left:0;top:0}
  .section-title{font-size:25px;font-weight:400;color:var(--white)}
  .contact{left:22px;top:980px;width:270px;color:var(--white)}
  .contact-row{display:flex;gap:14px;font-size:15px;line-height:22px;margin-top:8px}
  .contact-row svg{flex:none;margin-top:3px}
  .connect{margin-top:26px}
  .social{display:flex;gap:5px;margin-top:12px}
  .social span{width:27px;height:27px;background:var(--navy)}
  .social span:nth-child(2){background:#2aa3ef}
  .about{left:318px;top:976px;width:342px;color:var(--white)}
  .about p{margin-top:8px;font-size:15px;line-height:25px;text-align:justify}
  .footer{left:0;top:1243px;width:692px;height:52px;background:var(--footer);
    display:flex;align-items:center;justify-content:center;gap:10px;font-size:12.5px;color:#b9dcf2}
</style>
</head>
<body>
<div class="newsletter">
  <p class="abs preheader">You receive this email from Harbor Crest Advisory as we thought you might be interested in Harbor Crest Advisory programs.</p>
  <p class="abs preheader-right">Is this email not displaying correctly?<br><a href="#">View it in your browser.</a></p>

  <div class="abs hero-bg"></div>

  <svg class="abs shapes" width="692" height="1295" viewBox="0 0 692 1295" aria-hidden="true">
    <defs>
      <linearGradient id="heroBlue" x1="0" y1="0" x2="1" y2="1">
        <stop offset="0" stop-color="#1577db"/>
        <stop offset="1" stop-color="#0f8fe0"/>
      </linearGradient>
    </defs>
    <path d="M308 72 C300 210 250 300 160 378 C230 345 270 330 300 330 C320 420 410 478 510 476 C590 474 650 445 692 412 L692 72 Z" fill="url(#heroBlue)"/>
    <circle cx="358" cy="418" r="22" fill="none" stroke="#ffffff" stroke-width="6"/>
  </svg>

  <div class="abs brand"><span class="brand-dot"></span>Harbor Crest Advisory LLC</div>

  <div class="abs photo" role="img" aria-label="Smiling female doctor in white coat holding a clipboard and pen"></div>

  <h1 class="abs headline">
    <span class="hl-welcome">Welcome</span>
    <span class="hl-name">Harbor</span>
    <span class="hl-accent">Crest</span>
    <span class="hl-tail">Advisory</span>
  </h1>

  <h2 class="abs help-title">How Can We<br>Help You?</h2>

  <svg class="abs" style="left:0;top:0" width="692" height="1295" aria-hidden="true">
    <line x1="481" y1="620" x2="481" y2="900" stroke="#c9dbe8" stroke-width="1"/>
    <line x1="322" y1="756" x2="640" y2="756" stroke="#c9dbe8" stroke-width="1"/>
  </svg>

  <div class="service" style="left:357px;top:622px">
    <div class="service-icon" role="img" aria-label="First aid kit icon" style="background:#e4e7ea"></div>
    Revenue Cycle<br>Management</div>
  <div class="service" style="left:510px;top:618px">
    <div class="service-icon" role="img" aria-label="Doctor icon" style="background:#f6c089"></div>
    Compliance<br>Management</div>
  <div class="service" style="left:364px;top:780px">
    <div class="service-icon" role="img" aria-label="Brain and stethoscope icon" style="background:#e9566a"></div>
    Healthcare<br>Innovation</div>
  <div class="service" style="left:517px;top:780px">
    <div class="service-icon" role="img" aria-label="Person at desk icon" style="background:#f4c463"></div>
    Practice<br>Management</div>

  <svg class="abs lower" width="692" height="1295" viewBox="0 0 692 1295" aria-hidden="true">
    <defs>
      <linearGradient id="lowerBlue" x1="0" y1="0" x2="1" y2="0">
        <stop offset="0" stop-color="#1b7fe3"/>
        <stop offset="1" stop-color="#0a9ad6"/>
      </linearGradient>
    </defs>
    <path d="M0 912 C90 872 190 875 300 918 C420 966 560 962 692 925 L692 1295 L0 1295 Z" fill="url(#lowerBlue)"/>
    <path d="M300 918 C420 966 560 962 692 925" fill="none" stroke="#ffffff" stroke-width="4"/>
  </svg>

  <div class="abs call">
    <svg width="50" height="50" viewBox="0 0 24 24" aria-hidden="true">
      <path d="M6.6 10.8a15.1 15.1 0 0 0 6.6 6.6l2.2-2.2a1 1 0 0 1 1-.25 11.4 11.4 0 0 0 3.6.57 1 1 0 0 1 1 1V20a1 1 0 0 1-1 1A17 17 0 0 1 3 4a1 1 0 0 1 1-1h3.5a1 1 0 0 1 1 1c0 1.25.2 2.45.57 3.57a1 1 0 0 1-.25 1z" fill="#fff"/>
      <path d="M15 3.5a6 6 0 0 1 5.5 5.5M15 6.5a3 3 0 0 1 2.5 2.5" stroke="#fff" stroke-width="1.3" fill="none"/>
    </svg>
    <span class="call-label">CALL US</span>
    <span class="call-number">(555) 014-2290</span>
  </div>

  <div class="abs contact">
    <h3 class="section-title">Contact Us</h3>
    <div class="contact-row">
      <svg width="18" height="20" viewBox="0 0 24 24" aria-hidden="true"><path d="M12 2a7 7 0 0 0-7 7c0 5 7 13 7 13s7-8 7-13a7 7 0 0 0-7-7z" fill="none" stroke="#fff" stroke-width="1.8"/><circle cx="12" cy="9" r="2.5" fill="none" stroke="#fff" stroke-width="1.8"/></svg>
      <span>410 Larkspur Ave Suite 12, New York,<br>NY 10001, USA</span></div>
    <div class="contact-row">
      <svg width="18" height="18" viewBox="0 0 24 24" aria-hidden="true"><rect x="3" y="6" width="18" height="13" fill="none" stroke="#fff" stroke-width="1.8"/><path d="M3 7l9 7 9-7" fill="none" stroke="#fff" stroke-width="1.8"/></svg>
      <span>info@harborcrestadvisory.com</span></div>
    <div class="contact-row">
      <svg width="18" height="18" viewBox="0 0 24 24" aria-hidden="true"><path d="M6.6 10.8a15.1 15.1 0 0 0 6.6 6.6l2.2-2.2a1 1 0 0 1 1-.25 11.4 11.4 0 0 0 3.6.57 1 1 0 0 1 1 1V20a1 1 0 0 1-1 1A17 17 0 0 1 3 4a1 1 0 0 1 1-1h3.5a1 1 0 0 1 1 1c0 1.25.2 2.45.57 3.57a1 1 0 0 1-.25 1z" fill="none" stroke="#fff" stroke-width="1.6"/></svg>
      <span>(555) 014-2290</span></div>
    <h3 class="section-title connect" style="font-size:20px">Connect With Us</h3>
    <div class="social"><span></span><span></span><span></span></div>
  </div>

  <div class="abs about">
    <h3 class="section-title">About Us</h3>
    <p>Harbor Crest Advisory (HCA), founded in 2015, is a Management Services Organization &amp; Healthcare Consulting Firm skilled at helping medical practices advance their strategic vision in an ever-evolving healthcare system. Harbor Crest Advisory specializes in Revenue Cycle Management, Practice Management, Compliance Management &amp; Healthcare Innovation.</p>
  </div>

  <div class="abs footer">
    <span>www.harborcrestadvisory.com</span><span>|</span>
    <span>unsubscribe from the list</span><span>|</span>
    <span>Update Unsubscribe Preferences</span>
  </div>
</div>
</body>
</html>
```